Design for a newly formed Real Estate Management Company - Veltrona Management

Background
Veltrona Management is a Real Estate Company that manages properties for a small family business. I'd like to showcase the properties that I've acquired and turned around so they're performing well. This website will be a way for me to promote my business.

Different Sections
This website will help promote the work that I've been doing so it should include an About Us page. There should also be a page that goes through the different properties that we've managed and turned around. It would be great to have a design that allows me to visually show the different buildings that may be in various areas in a creative fashion. Finally, I need a section for a blog where I write about certain things prospective property owners should know about.

Design
http://www.qindaro7.example/ is a good example of the type of design I'm looking for. For the about us page, I'd like it to be able to show a portrait photo and a section to give some information about the person. I will be adding more people to the team so if there's a way to easily add photos and descriptions of new members, that would be great.

Target Market(s)

Third Party Real Estate Servicers (i.e. Insurance, Mortgage Brokers, Brokers)
Investors who are thinking to invest with us
Tenants who want to see how well we manage properties

Industry/Entity Type

Real Estate

Number of Pages Required

3 page

Requirements
Must have
• Integration of the logo into the design of the website would be a must. I'd like the design to flow together well and not be pages kind of stitched together. There should also be a way for me to easily add properties to the list. I should be able to monitor the people that join the website and obtain a login. It would be great to be able to edit and add things to the design so things aren't hardcoded.
Nice to have
• Allow tenants to write reviews of their experience at the property. Should not be anonymous, they would need to log in so at least their first name will show. Blog should also have log in so they may comment on the posts.

```html
<!DOCTYPE html>
<html lang="en">
<head>
<meta charset="utf-8">
<title>Veltrona Management</title>
<link href="https://fonts.googleapis.com/css2?family=Lato:wght@400;700;900&family=Open+Sans:wght@400;600;700&display=swap" rel="stylesheet">
<style>
:root{
  --blue:#2c65a1;
  --blue-dark:#1f4f82;
  --orange:#f2680c;
  --ink:#222;
  --muted:#9aa0a8;
  --text:#444;
  --band:#eef1f5;
  --panel:#2a2a2a;
  --footer:#0b0b0b;
  --blog-bg:#e9e9e9;
}
*{box-sizing:border-box;margin:0;padding:0}
html,body{width:1200px;height:2839px;overflow:hidden}
body{position:relative;background:#fff;font-family:"Open Sans",sans-serif;color:var(--text)}
.abs{position:absolute}
.topbar{left:0;top:0;width:1200px;height:38px;background:#f4f4f4;border-bottom:1px solid #e3e3e3}
.topbar .welcome{left:189px;top:12px;font-size:9px;color:#888;letter-spacing:.5px;font-weight:600}
.social-top{left:820px;top:0;display:flex}
.social-top span{width:38px;height:38px;border-left:1px solid #e1e1e1;display:flex;align-items:center;justify-content:center}
.social-top span i{width:10px;height:10px;background:#999;border-radius:2px;display:block}
.header{left:0;top:38px;width:1200px;height:72px;background:#fff}
.brand{left:189px;top:52px;display:flex;align-items:center;gap:10px}
.brand .mark{width:36px;height:36px;background:var(--blue)}
.brand .name{font-family:"Lato",sans-serif;font-weight:700;font-size:22px;color:#2a3a55;line-height:1}
.nav{left:552px;top:70px;display:flex;gap:30px;font-family:"Lato",sans-serif;font-size:14px;font-weight:700;color:var(--blue-dark)}
.nav .active{color:var(--blue)}
.call{left:878px;top:63px;display:flex;align-items:center;gap:6px}
.call .lbl{font-size:8px;color:#777;font-weight:700;line-height:1}
.call .num{font-family:"Lato",sans-serif;font-weight:900;font-size:19px;color:#2a3a55;line-height:1}
.hero{left:0;top:110px;width:1200px;height:448px;background:linear-gradient(100deg,#d9cfc2 0%,#b89a86 25%,#e7e3dc 55%,#cfc9c0 100%)}
.signup{left:765px;top:199px;width:250px;height:366px;background:var(--panel);padding:20px 22px}
.signup h2{font-family:"Lato",sans-serif;color:#fff;font-weight:700;font-size:17px;line-height:1.1}
.signup h2 b{display:block;font-size:32px;font-weight:900}
.signup label{display:block;color:#fff;font-size:10px;font-weight:700;margin-top:16px;margin-bottom:5px}
.signup .field{height:35px;background:#fff}
.signup .btn{margin-top:16px;height:40px;background:var(--orange);color:#fff;font-weight:700;font-size:14px;display:flex;align-items:center;justify-content:center}
.signup .req{color:#bbb;font-size:9px;margin-top:8px}
.section-title{left:0;width:1200px;text-align:center;font-family:"Lato",sans-serif;font-weight:900;font-size:21px;color:var(--ink)}
.section-sub{left:300px;width:600px;text-align:center;font-size:10px;line-height:22px;color:var(--muted)}
.band{left:0;top:691px;width:1200px;height:473px;background:var(--band)}
.tabs{left:157px;top:738px;width:841px;height:80px;background:#fff;display:flex;align-items:center;padding-left:81px}
.tabs span{width:103px;height:32px;display:flex;align-items:center;justify-content:center;font-size:11px;color:var(--blue);font-weight:600}
.tabs .on{background:var(--blue);color:#fff}
.prop-photo{left:189px;top:838px;width:388px;height:309px;background:#fff;border:1px solid #ddd;padding:8px}
.prop-photo div{width:100%;height:100%;background:linear-gradient(180deg,#6a9bd3 0%,#a9c3df 35%,#b6a48e 60%,#4f8a37 100%)}
.loc-head{left:605px;top:838px;width:240px;height:38px;background:#fff;font-family:"Lato",sans-serif;font-weight:900;font-size:14px;color:var(--ink);padding:12px 6px}
.loc-text{left:610px;top:880px;width:405px;font-size:10px;line-height:22px;color:var(--muted)}
.feat{left:612px;width:410px;display:flex;gap:16px}
.feat .ic{width:42px;height:42px;border-radius:50%;background:var(--blue);flex:none;display:flex;align-items:center;justify-content:center}
.feat h4{font-size:11px;font-weight:700;color:var(--ink);margin-top:-2px;margin-bottom:4px}
.feat p{font-size:10px;line-height:20px;color:var(--muted)}
.gallery{left:0;top:1370px;width:1200px;height:413px}
.gallery div{position:absolute;height:205px}
.sec-head{display:flex;align-items:center;gap:14px;font-family:"Lato",sans-serif;font-weight:900;font-size:20px;color:var(--ink)}
.happy-img{left:189px;top:1927px;width:191px;height:144px;border:1px solid #ddd;padding:4px;background:#fff}
.happy-img div{width:100%;height:100%;background:linear-gradient(160deg,#9cb6c9,#b68a64 55%,#6d7f3e)}
.happy-text{left:398px;top:1926px;width:270px;font-size:10px;line-height:15px;color:#333}
.links{left:398px;top:2003px;font-size:10px;font-weight:700;color:#222}
.links li{list-style:none;line-height:24px;text-decoration:underline}
.links li::before{content:"›";margin-right:8px;text-decoration:none;display:inline-block}
.review{left:713px;top:1926px;width:302px;height:89px;border:1px solid #ccc;padding:14px 14px;font-size:10px;line-height:15px;color:#333}
.dots{left:716px;top:2057px;display:flex;gap:4px}
.dots i{width:5px;height:5px;border-radius:50%;background:#ccc;display:block}
.dots i:first-child{background:#333}
.rev-by{left:815px;top:2044px;width:200px;text-align:right;font-size:11px;line-height:18px;color:#333}
.rev-by b{display:block;color:var(--blue);font-weight:600}
.tweets{left:0;top:2173px;width:477px;height:381px;background:var(--blue)}
.blog{left:477px;top:2173px;width:723px;height:381px;background:var(--blog-bg)}
.h-white{font-family:"Lato",sans-serif;font-weight:900;font-size:21px;color:#fff}
.tweet{left:189px;width:260px;font-size:10px;line-height:13px;color:#a9c6e8}
.tweet b{display:block;color:#fff;font-weight:700;font-size:11px;margin-bottom:2px}
.tweet em{display:block;font-style:normal;color:#fff;margin-top:12px}
.follow{left:189px;top:2480px;width:124px;height:36px;border:2px solid #fff;color:#fff;font-weight:700;font-size:12px;display:flex;align-items:center;justify-content:center;gap:8px}
.follow i{width:10px;height:10px;background:#fff;display:block}
.post-img{left:517px;width:161px;height:111px;background:#fff;border:1px solid #ccc;padding:4px}
.post-img div{width:100%;height:100%}
.post{left:696px;width:300px;font-size:10px;line-height:15px;color:#333}
.post h5{font-size:11px;font-weight:700;color:var(--blue);margin-bottom:12px}
.post .meta{color:var(--blue);font-weight:700;font-size:9px;margin-top:18px}
.footer{left:0;top:2554px;width:1200px;height:285px;background:var(--footer)}
.f-head{top:2608px;font-family:"Lato",sans-serif;font-weight:900;font-size:14px;color:var(--orange)}
.f-text{font-size:9px;line-height:17px;color:#ccc}
.f-text b{color:#fff}
.nl-input{left:862px;top:2644px;width:118px;height:24px;background:#fff;font-size:9px;color:#333;padding:6px}
.nl-btn{left:862px;top:2681px;width:82px;height:26px;background:var(--blue);color:#fff;font-weight:700;font-size:12px;display:flex;align-items:center;justify-content:center}
.circles{left:686px;top:2685px;display:flex;gap:5px}
.circles i{width:20px;height:20px;border:1px solid #ccc;border-radius:50%;display:block}
.f-rule{left:189px;top:2797px;width:826px;height:1px;background:#333}
.copy{left:189px;top:2811px;font-size:9px;color:#ccc}
.legal{left:868px;top:2811px;font-size:9px;color:#ccc;display:flex;gap:10px}
</style>
</head>
<body>

<div class="abs topbar">
  <div class="abs welcome">WELCOME TO LUMENHAVEN - A SINGLE PROPERTY THEME</div>
  <div class="abs social-top"><span><i></i></span><span><i></i></span><span><i></i></span><span><i></i></span><span style="border-right:1px solid #e1e1e1"><i></i></span></div>
</div>

<header class="abs header"></header>
<div class="abs brand"><span class="mark"></span><span class="name">Veltrona Management</span></div>
<nav class="abs nav"><span class="active">Home</span><span>About Us</span><span>Blog</span><span>Contact Us</span></nav>
<div class="abs call">
  <svg width="20" height="20" viewBox="0 0 24 24"><path d="M6.6 10.8a15 15 0 0 0 6.6 6.6l2.2-2.2c.3-.3.7-.4 1-.2 1.1.4 2.3.6 3.6.6.6 0 1 .4 1 1V20c0 .6-.4 1-1 1A17 17 0 0 1 3 4c0-.6.4-1 1-1h3.5c.6 0 1 .4 1 1 0 1.3.2 2.5.6 3.6.1.3 0 .7-.2 1z" fill="#2a3a55"/></svg>
  <div><div class="lbl">CALL US NOW</div><div class="num">555-010-4567</div></div>
</div>

<div class="abs hero" role="img" aria-label="Photo of a smiling couple embracing in a bright home interior"></div>
<form class="abs signup">
  <h2>Welcome to your<b>New Living!</b></h2>
  <label>Your Name*</label><div class="field"></div>
  <label>Your Email*</label><div class="field"></div>
  <label>Your Phone*</label><div class="field"></div>
  <div class="btn">Get Notified!</div>
  <div class="req">*Required Fields</div>
</form>

<h2 class="abs section-title" style="top:650px">FEATURED PROJECTS &amp; PROPERTIES</h2>
<div class="abs band"></div>
<p class="abs section-sub" style="top:690px">Lorem ipsum dolor sit amet, consectetur adipiscing elit. Sed tempor arcu non ligula convallis, vel tincidunt ipsum posuere.sollicitudin. Duis iaculis, arcu ut hendrerit pharetra, elit augue pulvinar magna</p>
<div class="abs tabs"><span class="on">Location 1</span><span>Location 2</span><span>Location 3</span><span>Location 4</span><span>Location 5</span><span>Location 6</span><span>Location 7</span></div>
<div class="abs prop-photo"><div role="img" aria-label="Photo of a two-storey suburban house with garage and front lawn"></div></div>
<div class="abs loc-head">LOCATION 1</div>
<p class="abs loc-text">Lorem ipsum dolor sit amet, consectetur adipiscing elit. Sed tempor arcu non ligula convallis, vel tincidunt ipsum posuere.sollicitudin. Duis iaculis, arcu ut hendrerit pharetra, elit augue pulvinar magna</p>
<div class="abs feat" style="top:969px">
  <span class="ic"><svg width="16" height="16" viewBox="0 0 16 16"><path d="M8 1C4 5 4 10 8 15c4-5 4-10 0-14zM8 4v10" stroke="#fff" stroke-width="1.4" fill="none"/></svg></span>
  <div><h4>Nature</h4><p>Lorem ipsum dolor sit amet, consectetur adipiscing elit. Sed tempor arcu non ligula convallis, vel tincidunt.</p></div>
</div>
<div class="abs feat" style="top:1066px">
  <span class="ic"><svg width="18" height="12" viewBox="0 0 18 12"><path d="M2 7l2-4h10l2 4v3H2z" stroke="#fff" stroke-width="1.4" fill="none"/><circle cx="5" cy="10" r="1.4" fill="#fff"/><circle cx="13" cy="10" r="1.4" fill="#fff"/></svg></span>
  <div><h4>Car parking</h4><p>Lorem ipsum dolor sit amet, consectetur Sed tempor arcu non ligula convallis, vel tincidunt.</p></div>
</div>

<h2 class="abs section-title" style="top:1241px">PHOTO GALLERY</h2>
<p class="abs section-sub" style="top:1282px">Lorem ipsum dolor sit amet, consectetur adipiscing elit. Sed tempor arcu non ligula convallis, vel tincidunt ipsum posuere.sollicitudin. Duis iaculis, arcu ut hendrerit pharetra, elit augue pulvinar magna</p>
<div class="abs gallery">
  <div role="img" aria-label="Bedroom with white bed and red pillows" style="left:0;top:0;width:184px;background:linear-gradient(160deg,#5b5148,#e8e2dc)"></div>
  <div role="img" aria-label="Living room with white sofas and rug" style="left:186px;top:0;width:274px;background:linear-gradient(160deg,#b9a88f,#e9e1d4)"></div>
  <div role="img" aria-label="Pool and palm trees at sunset" style="left:462px;top:0;width:274px;background:linear-gradient(180deg,#e9b25d,#6d7b45 60%,#3c8fa3)"></div>
  <div role="img" aria-label="Modern steel kitchen" style="left:738px;top:0;width:275px;background:linear-gradient(160deg,#7e7a74,#d9d4cc)"></div>
  <div role="img" aria-label="Bright living room with white walls" style="left:1015px;top:0;width:185px;background:linear-gradient(160deg,#d8dde2,#b79c7a)"></div>
  <div role="img" aria-label="Kitchen with wood cabinets" style="left:0;top:207px;width:184px;background:linear-gradient(160deg,#6a5040,#b9b1a6)"></div>
  <div role="img" aria-label="Lit house with pool at dusk" style="left:186px;top:207px;width:274px;background:linear-gradient(180deg,#4a6e9a,#8a6a48 60%,#3cb0d0)"></div>
  <div role="img" aria-label="Lounge with chairs and fireplace" style="left:462px;top:207px;width:274px;background:linear-gradient(160deg,#3d2a1e,#b9814b)"></div>
  <div role="img" aria-label="Gym with exercise machines" style="left:738px;top:207px;width:275px;background:linear-gradient(160deg,#e7e7e7,#8a8a8a)"></div>
  <div role="img" aria-label="Children jumping into a pool" style="left:1015px;top:207px;width:185px;background:linear-gradient(160deg,#4d8fd0,#2ab0d9)"></div>
</div>

<div class="abs sec-head" style="left:190px;top:1876px">
  <svg width="28" height="28" viewBox="0 0 28 28"><circle cx="14" cy="14" r="12" stroke="#2c65a1" stroke-width="2" fill="none"/><circle cx="10" cy="11" r="1.5" fill="#2c65a1"/><circle cx="18" cy="11" r="1.5" fill="#2c65a1"/><path d="M8 16a6 6 0 0 0 12 0" stroke="#2c65a1" stroke-width="2" fill="none"/></svg>
  WE ARE HAPPY WITH YOU
</div>
<div class="abs happy-img"><div role="img" aria-label="Photo of a hiking couple outdoors"></div></div>
<p class="abs happy-text">Suspendisse potenti. Proin lobortis tortor eget eros tincidunt fermentum. Suspendisse nec sapien non arcu viverra volutpat eget ac nulla. Fusce consequat pellen tesque ex, at pellentesque nunc scelerisque eget.</p>
<ul class="abs links"><li>Lorem ipsum dolor sit amet, consectetur adipiscing</li><li>Lorem ipsum dolor sit amet, consectetur adipiscing</li><li>Lorem ipsum dolor sit amet, consectetur adipiscing</li></ul>

<div class="abs sec-head" style="left:712px;top:1876px">
  <svg width="24" height="28" viewBox="0 0 24 28"><rect x="2" y="2" width="20" height="24" stroke="#2c65a1" stroke-width="2" fill="none"/><path d="M6 9h12M6 14h12M6 19h12" stroke="#2c65a1" stroke-width="2"/></svg>
  CLIENT REVIEWS
</div>
<p class="abs review">Suspendisse potenti. Proin lobortis tortor eget eros tincidunt fermentum. Suspendisse nec sapien non arcu viverra volutpat eget ac nulla. Fusce consequat pellen tesque ex, at pellentesque nunc .</p>
<div class="abs dots"><i></i><i></i><i></i></div>
<div class="abs rev-by">Lorem ipsum<b>Vivamus porttitor turpis</b></div>

<div class="abs tweets"></div>
<h3 class="abs h-white" style="left:189px;top:2222px">RECENT TWEETS</h3>
<p class="abs tweet" style="top:2274px"><b>Veltrona Realestate</b>Lorem Ipsum is simply dummy text of the printing and typesetting industry. Lorem Ipsum has been the industry's standard dummy text ever since the 1500s<em>Posted on 23 jan</em></p>
<p class="abs tweet" style="top:2374px"><b>Veltrona Realestate</b>Lorem Ipsum is simply dummy text of the printing and typesetting industry. Lorem Ipsum has been the industry's standard dummy text ever since the 1500s<em>Posted on 23 jan</em></p>
<div class="abs follow"><i></i>Follow Us</div>

<div class="abs blog"></div>
<h3 class="abs h-white" style="left:515px;top:2222px;color:#222">RECENT FROM BLOG</h3>
<div class="abs post-img" style="top:2275px"><div role="img" aria-label="Photo of a suburban house" style="background:linear-gradient(180deg,#8fb1d6,#b5a48c 55%,#5a8b3c)"></div></div>
<div class="abs post" style="top:2273px"><h5>UNIVERSITY NEAR TO MARLOWE VILLA</h5>Suspendisse potenti. Proin lobortis tortor eget eros tincidunt fermentum. Suspendisse nec sapien non arcu viverra volutpat eget ac nulla...<div class="meta">May 20,2015 Lumen Villa 4 comments</div></div>
<div class="abs post-img" style="top:2405px"><div role="img" aria-label="Photo of a bright living room" style="background:linear-gradient(160deg,#3a3a3a,#e6e2dc)"></div></div>
<div class="abs post" style="top:2403px"><h5>UNIVERSITY NEAR TO MARLOWE VILLA</h5>Suspendisse potenti. Proin lobortis tortor eget eros tincidunt fermentum. Suspendisse nec sapien non arcu viverra volutpat eget ac nulla...<div class="meta">May 20,2015 Lumen Villa 4 comments</div></div>

<footer class="abs footer"></footer>
<h4 class="abs f-head" style="left:186px">LATEST NEWS</h4>
<p class="abs f-text" style="left:186px;top:2638px;width:220px">New Blog Post - Orvale-Brent Teams Up With Roomwise for Stonefield Athletic Storage Contest <b>http://ln.example/a1</b> 12</p>
<div class="abs" style="left:186px;top:2703px;width:210px;height:1px;background:#333"></div>
<p class="abs f-text" style="left:186px;top:2712px;width:220px">New Blog Post - Fort Kelbury Football Adds Finishing Touches to a First Class Program <b>http://ln.example/b2</b> 42 mins ago</p>
<h4 class="abs f-head" style="left:498px">SUPPORT</h4>
<p class="abs f-text" style="left:498px;top:2638px">About us<br>Privacy Policy<br>Terms &amp; Conditions<br>Resources</p>
<h4 class="abs f-head" style="left:681px">CONTACT US</h4>
<p class="abs f-text" style="left:686px;top:2636px">✉ info@veltrona.example<br>☎ 555-010-6855</p>
<div class="abs circles"><i></i><i></i><i></i></div>
<h4 class="abs f-head" style="left:858px">NEWSLETTER</h4>
<div class="abs nl-input">Email Address</div>
<div class="abs nl-btn">Submit</div>
<div class="abs f-rule"></div>
<div class="abs copy">© 2015 Veltrona Management</div>
<div class="abs legal"><span>Understand</span><span>Disable</span><span>Cookies</span></div>

</body>
</html>
```